Need label design for car cleaning spray bottle, big opportunity for repeat work

This is the first label design for a large assortment of car cleaning products. This design will be vital as it will set the design style for the remaining products. There is large opportunity for repeat work to the winning designer. For this first product we plan to call it "Interior Cleaner". We have the template label which we have attached to the project. The product is geared towards the market of Volmara car owners, and our logo also utilizes a similar font to what Volmara's company font uses.

We are looking to only update the design/format of the label. We will keep all text the same or modify it once the design is final. We will need to use our brand logo (attached).

We are looking for a minimalistic style design. Currently the label reads horizontally but we have noticed that the most successful brands that sell online have a vertical style design. We have attached some examples of brands such as "Gleam Bastion" and "Pivlo" which sell primarily on shopvendrix.com and have tens of thousands of reviews. We'd like to try and copy this label format as it seems very successful for these brands.

We are big fans of the minimal style that the brand "AutoZell" uses. Their label design emphasizes the name of the particular product in black text on a white background. The remainder of the label is color coded, and all of their products have a different color code while following the same diagonal design style. See attached examples.

So that being said, we would like to combine these 2 concepts, vertical alignment style with the minimalistic label design.

We are thinking of making the entire label white, and having an accent color like 1 large stripe that goes across the bottle, it would be an iconic part of the design as we will repeat this design across multiple products, similar to the AutoZell brand bundle example we attached. This specific product will be pink liquid (as you can tell the accent color is pink on the label).

We'd like to add a dynamic QR code (can use placeholder) on the label so customers can be directed to our website easily or any other page we choose in the future. We will also need a UPC barcode label (can use placeholder)

Target Market(s)

Volmara car owners

Industry/Entity Type

Car Detailing Products

Font styles to use
Sans Serif

Colors
E54698
E96AAD
F1A4CE
F9D9EA
FCEFF6

Requirements
Must have
• minimalistic design
Should not have
• no designs similar to brands like polish crew, dravonels, or any older brands in the category

```html
<!DOCTYPE html>
<html lang="en">
<head>
<meta charset="utf-8">
<title>Korvelle Interior Cleaner – Label Options</title>
<link rel="stylesheet" href="https://fonts.googleapis.com/css2?family=Montserrat:wght@300;500;700;800;900&display=swap">
<style>
  :root {
    --backdrop: #c9c9c9;
    --label-white: #ffffff;
    --ink: #111111;
    --pink-strong: #e54698;
    --pink-mid: #e96aad;
    --pink-soft: #f1a4ce;
    --pink-pale: #f9d9ea;
    --pink-mist: #fceff6;
  }
  * { box-sizing: border-box; margin: 0; padding: 0; }
  html, body { width: 1200px; height: 800px; overflow: hidden; }
  body {
    background: radial-gradient(ellipse at 50% 50%, #dedede 0%, var(--backdrop) 60%, #b4b4b4 100%);
    font-family: "Montserrat", Arial, sans-serif;
    color: var(--ink);
    position: relative;
  }
  .option {
    position: absolute;
    top: 40px;
    width: 230px;
    text-align: center;
  }
  .option--one { left: 288px; }
  .option--two { left: 642px; }
  .option__title {
    font-weight: 500;
    font-size: 17px;
    letter-spacing: 0.5px;
    margin-bottom: 150px;
  }
  .label {
    position: relative;
    width: 230px;
    height: 520px;
    background: var(--label-white);
    overflow: hidden;
    box-shadow: 0 8px 24px rgba(0,0,0,0.12);
  }
  .label__top-band {
    position: absolute;
    top: 0; left: 0;
    width: 100%; height: 36px;
    background: linear-gradient(90deg, var(--pink-mid), var(--pink-strong) 50%, var(--pink-mid));
  }
  .label__brand {
    position: absolute;
    left: 0; right: 0;
    top: 24px;
    font-weight: 500;
    font-size: 19px;
    line-height: 1;
    letter-spacing: 2.5px;
  }
  .label--banded .label__brand { top: 54px; }
  .label__brand::after {
    content: "";
    display: inline-block;
    width: 5px; height: 5px;
    border-radius: 50%;
    background: var(--ink);
    margin-left: 3px;
    vertical-align: top;
  }
  .label__name {
    position: absolute;
    left: 66px;
    bottom: 122px;
    writing-mode: vertical-rl;
    transform: rotate(180deg);
    text-align: start;
    line-height: 1;
    white-space: nowrap;
  }
  .label--banded .label__name { bottom: 120px; }
  .label__variant {
    display: block;
    font-weight: 300;
    font-size: 24px;
    letter-spacing: 4px;
    margin-left: 4px;
    padding-top: 52px;
  }
  .label__product {
    display: block;
    font-weight: 900;
    font-size: 56px;
    letter-spacing: -1px;
  }
  .label__band {
    position: absolute;
    left: 0; bottom: 0;
    width: 230px; height: 180px;
  }
  .badge {
    position: absolute;
    width: 54px; height: 54px;
    border-radius: 50%;
    background: var(--ink);
    border: 3px solid var(--pink-pale);
    color: var(--label-white);
    display: flex;
    flex-direction: column;
    align-items: center;
    justify-content: center;
    font-weight: 800;
    line-height: 1.05;
    text-align: center;
  }
  .badge span { display: block; }
  .badge .badge__small { font-size: 6px; font-weight: 700; }
  .badge .badge__big { font-size: 9px; }
  .badge--acid { left: 12px; bottom: 32px; }
  .badge--surface { left: 88px; bottom: 50px; }
  .badge--grime { left: 164px; bottom: 80px; }
  .label__net {
    position: absolute;
    left: 0; right: 0;
    bottom: 10px;
    font-size: 6.5px;
    font-weight: 500;
    letter-spacing: 0.5px;
    color: var(--pink-pale);
  }
</style>
</head>
<body>

  <section class="option option--one">
    <h2 class="option__title">OPTION 1</h2>
    <div class="label">
      <p class="label__brand">KORVELLE</p>
      <h1 class="label__name">
        <span class="label__variant">INTERIOR</span>
        <span class="label__product">CLEANER</span>
      </h1>
      <svg class="label__band" viewBox="0 0 230 180" role="img" aria-label="Pink accent band with a fine chevron texture">
        <defs>
          <linearGradient id="band-fill-one" x1="0" y1="0" x2="1" y2="1">
            <stop offset="0" stop-color="#e96aad"/>
            <stop offset="0.6" stop-color="#e54698"/>
            <stop offset="1" stop-color="#d83d8c"/>
          </linearGradient>
        </defs>
        <path d="M0 88 C 80 70, 150 40, 230 0 L230 180 L0 180 Z" fill="#f9d9ea"/>
        <path d="M0 96 C 80 80, 150 54, 230 16 L230 180 L0 180 Z" fill="url(#band-fill-one)"/>
      </svg>
      <div class="badge badge--acid"><span class="badge__big">NON</span><span class="badge__big">ACIDIC</span><span class="badge__small">FORMULA</span></div>
      <div class="badge badge--surface"><span class="badge__small">INTERIOR</span><span class="badge__big">AND</span><span class="badge__small">EXTERIOR</span></div>
      <div class="badge badge--grime"><span class="badge__small">REMOVES</span><span class="badge__small">GREASE</span><span class="badge__big">GRIME</span><span class="badge__big">&amp; DIRT</span></div>
      <p class="label__net">NET CONTENTS: 16 FL. OZ. (473ML)</p>
    </div>
  </section>

  <section class="option option--two">
    <h2 class="option__title">OPTION 2</h2>
    <div class="label label--banded">
      <div class="label__top-band" role="img" aria-label="Pink top band with a fine chevron texture"></div>
      <p class="label__brand">KORVELLE</p>
      <h1 class="label__name">
        <span class="label__variant">INTERIOR</span>
        <span class="label__product">CLEANER</span>
      </h1>
      <svg class="label__band" viewBox="0 0 230 180" role="img" aria-label="Pink accent band with a fine chevron texture">
        <defs>
          <linearGradient id="band-fill-two" x1="0" y1="0" x2="1" y2="1">
            <stop offset="0" stop-color="#e96aad"/>
            <stop offset="0.6" stop-color="#e54698"/>
            <stop offset="1" stop-color="#d83d8c"/>
          </linearGradient>
        </defs>
        <path d="M0 88 C 80 70, 150 40, 230 0 L230 180 L0 180 Z" fill="#f9d9ea"/>
        <path d="M0 96 C 80 80, 150 54, 230 16 L230 180 L0 180 Z" fill="url(#band-fill-two)"/>
      </svg>
      <div class="badge badge--acid"><span class="badge__big">NON</span><span class="badge__big">ACIDIC</span><span class="badge__small">FORMULA</span></div>
      <div class="badge badge--surface"><span class="badge__small">INTERIOR</span><span class="badge__big">AND</span><span class="badge__small">EXTERIOR</span></div>
      <div class="badge badge--grime"><span class="badge__small">REMOVES</span><span class="badge__small">GREASE</span><span class="badge__big">GRIME</span><span class="badge__big">&amp; DIRT</span></div>
      <p class="label__net">NET CONTENTS: 16 FL. OZ. (473ML)</p>
    </div>
  </section>

</body>
</html>
```